Packaging design for children’s shampoo bar

A design that could be used on solid shampoo and soap wraps then amended for jar labels. The packaging needs to be bright and child-friendly. We have a logo and a pattern, but please feel free to change them. I think it needs to be brighter.

I would like each product to have an accent colour and for the shampoo I am thinking of blue/teal. This will be complemented by the body wash bar (pink) and toothpaste (orange).

The shampoo bar wrap needs to contain the following information:

Pippa & Pals logo
Shampoo Bar
100% natural
Vegan & Palm Oil-Free
Weight 85 g
Made in the U.K.

Ingredients: sodium hydroxide, prunus amygdalus dulcis oil, olea europaea oil, cocos nucifera oil, ricinus communis seed oil, simmondsia chinensia seed oil.

Contact details: Pippa & Pals, Marden Oakley House, London N7 4QB. Website: www.Pippa and pals.co.U.K.

Brand board is here: https://www.filevaultex.com/s/k8rw2tqumezbvyx/Photo%2003-07-2020%2C%2021%2040%2034.jpg?dl=0

Inspiration is here: https://kitemoorstudio.co.uk/collections/beauty-grooming/products/dog-shampoo-100-natural-vegan

These are the wraps we shall be using: https://www.brightwickpress.co.uk/soap-wrap

Thank you so much for your interest in this project!

Target Market(s)

Children 5-12 years.

Requirements
Must have
• Clean design. Lots of white with bright colours.

```html
<!DOCTYPE html>
<html lang="en">
<head>
<meta charset="utf-8">
<title>Pippa &amp; Pals – Shampoo Bar Wrap</title>
<link rel="stylesheet" href="https://fonts.googleapis.com/css2?family=Gaegu:wght@700&family=Lato:wght@400;700;900&family=Roboto:wght@300&display=swap">
<style>
  :root {
    --stage: #e6e7e7;
    --wrap-edge: #a9d3de;
    --wrap-mid: #f4f6f6;
    --accent-blue: #8ccbdf;
    --ink-grey: #666666;
    --ink-dark: #1e1e1e;
    --brand-coral: #e98b6a;
    --pill-grey: #8a8a8a;
    --white: #ffffff;
  }
  * { box-sizing: border-box; margin: 0; padding: 0; }
  html, body {
    width: 1200px; height: 841px; overflow: hidden;
    background: var(--stage);
  }
  .sheet {
    position: relative; width: 1200px; height: 841px;
  }
  .wrap-panel {
    position: absolute; left: 294px; width: 612px; height: 375px;
    border-radius: 8px; overflow: hidden;
    box-shadow: 0 2px 6px rgba(0,0,0,0.12);
    text-align: center;
  }
  .wrap-panel--front { top: 38px; }
  .wrap-panel--back { top: 425px; }
  .wrap-pattern {
    position: absolute; inset: 0;
    background:
      radial-gradient(ellipse 60% 70% at 50% 50%, var(--wrap-mid) 0%, rgba(244,246,246,0.85) 45%, rgba(244,246,246,0) 85%),
      linear-gradient(180deg, #d8ecf1 0%, var(--wrap-edge) 100%);
  }
  .wrap-content { position: relative; }
  .brand-name {
    display: inline-flex; align-items: center; gap: 10px;
    margin-top: 70px;
    font-family: "Gaegu", cursive; font-weight: 700;
    font-size: 56px; line-height: 1; color: var(--brand-coral);
  }
  .brand-dot {
    width: 18px; height: 18px; border-radius: 50%; background: var(--brand-coral);
  }
  .claim {
    font-family: "Lato", sans-serif; font-weight: 900;
    color: var(--accent-blue); letter-spacing: 0.5px;
  }
  .product-name {
    font-family: "Gaegu", cursive; font-weight: 700;
    color: var(--ink-grey); letter-spacing: 3px; line-height: 1;
  }
  .wrap-panel--front .claim { font-size: 24px; margin-top: 38px; }
  .wrap-panel--front .product-name { font-size: 66px; margin-top: 2px; }
  .tagline {
    font-family: "Roboto", sans-serif; font-weight: 300;
    font-size: 16px; color: var(--ink-grey); margin-top: 14px;
  }
  .wrap-panel--back .claim { font-size: 15px; margin-top: 58px; }
  .wrap-panel--back .product-name { font-size: 40px; margin-top: 0; }
  .ingredients, .contact {
    font-family: "Lato", sans-serif; font-size: 12px; line-height: 1.4;
    color: var(--ink-dark);
  }
  .ingredients { width: 440px; margin: 12px auto 0; }
  .ingredients strong { font-weight: 700; }
  .contact { margin-top: 16px; }
  .contact-name { font-weight: 700; font-size: 13px; }
  .origin {
    font-family: "Lato", sans-serif; font-weight: 900; font-size: 7px;
    letter-spacing: 0.3px; color: var(--ink-dark); margin-top: 2px;
  }
  .weight-pill {
    display: inline-block; margin-top: 12px; padding: 2px 8px;
    border-radius: 9px; background: var(--pill-grey);
    font-family: "Roboto", sans-serif; font-weight: 300;
    font-size: 11px; color: var(--white);
  }
</style>
</head>
<body>
<main class="sheet">
  <section class="wrap-panel wrap-panel--front">
    <div class="wrap-pattern" role="img" aria-label="Pale blue wrap background with a faint pattern of jungle animals, leaves and rainbows"></div>
    <div class="wrap-content">
      <div class="brand-name"><span>Pippa &amp; Pals</span><span class="brand-dot"></span></div>
      <p class="claim">100% NATURAL</p>
      <h1 class="product-name">SHAMPOO BAR</h1>
      <p class="tagline">Vegan &amp; Palm Oil-Free</p>
    </div>
  </section>

  <section class="wrap-panel wrap-panel--back">
    <div class="wrap-pattern" role="img" aria-label="Pale blue wrap background with a faint pattern of jungle animals, leaves and rainbows"></div>
    <div class="wrap-content">
      <p class="claim">100% NATURAL</p>
      <h2 class="product-name">SHAMPOO BAR</h2>
      <p class="ingredients"><strong>Ingredients:</strong> Sodium hydroxide, prunus amygdalus dulcis oil, olea europaea oil, cocos nucifera oil, ricinus communis seed oil, simmondsia chinensia seed oil.</p>
      <div class="contact">
        <p class="contact-name">Pippa &amp; Pals</p>
        <p>Marden Oakley House, London N7 4QB.</p>
        <p>Website: www.Pippa and pals.co.U.K.</p>
      </div>
      <p class="origin">MADE IN THE U.K.</p>
      <span class="weight-pill">WEIGHT 85 G</span>
    </div>
  </section>
</main>
</body>
</html>
```